Video Thumbnail Design for Jazz Piano YouTube channel

Hello, my name’s Marcus Fenwick. I run a jazz piano YouTube channel called ‘Keyset Lessons’ (www.vidloop-example.com/keysetlessons). It’s the most subscribed to jazz piano YouTube channel with over 200,000 subscribers.

I need a designer to create an eye-catching thumbnail, to be used for my upcoming videos.

BRIEF:
For now, I’m asking for just one thumbnail design. I will choose a designer from this initial project, and I plan to commission additional designs from the same designer - so that my thumbnails all have a coherent look.

WHAT MAKES A GOOD THUMBNAIL:
Above all, your thumbnail design must be EYE-CATCHING and STAND OUT. Imagine scrolling through hundreds of YouTube videos - the video’s thumbnail artwork is one of the key aspects that gets someone to click and watch a video, so this is a VERY important aspect to getting views.

Your design can be innovative - surprise me. I want your design to JUMP OUT at me. For example, you could experiment with creating a 3D effect, or having elements popping out of the frame. A YouTube thumbnail doesn’t have to be square to the edges - you can add white around the edges to create an unusual jagged effect (when viewed in YouTube's search, which has a white background), and certain things could come out of the picture (see attached files for reference).

Remember, YouTube thumbnails are displayed very small - especially on desktop. It’s a good idea to design your thumbnail at this small size, rather than at full size on your computer screen. You'll probably need to zoom in closer to my face and enlarge the text more than you normally would if you were creating a larger image.

Lots of contrast is needed in a tiny thumbnail. Blacks must be pitch black, whites must be white, color saturation - the thumbnail must contain a lot of energy in a small space.

A strong format for YouTube thumbnails is to have a FACE (my face) and TEXT (large white text, 3 - 5 words). You can use this if you like, or you can experiment with a different format. I’m completely open to your ideas.

BRAND LOOK & FEEL:
Here are some keywords that describe my brand:
- Calm
- Professional
- Sophisticated (jazz is a sophisticated style of music)
View my channel to see my visual style as a starting point: www.vidloop-example.com/keysetlessons

BRAND COLORS:
- Turquoise: Hex #00DBD7 (this is my main brand color and must be used in the thumbnail)
- Black
- White
- Red: #FC5B5B (I sometimes use this as a secondary color - you can use this in your design if you want, or not).

TEXT:
The font I use for my brand is ‘Lovelo’ (please use this font in your design - included in my attachment).
I like my text to be white against a black background.
For your design, you could use the text: 'SWEET CHORD VOICING' as sample text.

IMAGES:
I've attached several photos for you to work with - just choose one for your design. The backgrounds are not important to the Thumbnail - only me and the piano are needed - so it's up to you whether you black out the background, darken it, or leave it in. Feel free to zoom in, rotate at an angle, distort, etc.

SLANTS:
I like diagonal lines and slants - because they go well with the ‘jazz’ feel. This could include the text itself (at an angle instead of straight), or the picture (any images of me or the piano could be at an angle, rather than straight).

DIMENSIONS:
YouTube thumbnails must be 1280 pixels wide by 720 pixels tall. A ratio of 16:9 is ideal as it’s used most often in YouTube players and previews.

DELIVERABLES:
If your design is selected - I will need a Photoshop file delivered of the final design (this is so that I can edit the text myself to make it relevant to the video).

After that, I will commission further designs with you (these will be separate projects, each with its own payment). My end goal is to have 10 - 15 strong thumbnail designs - all from the same designer.

Thank you very much for your submission, I can't wait to see what you come up with!

Target Market(s)

My audience is 90% male, between 25 - 65 years old. I have viewers worldwide, but they mostly live in the US and Canada.

Font styles to use
Other font styles liked:
• Lovelo

Colors
31b7a3

Requirements
Must have
• Image and text (as described in the project description)
Nice to have
• Creative use of white edges to stand out on YouTube (against other traditional square looking thumbnails).
• See full description in the project description.

```html
<!DOCTYPE html>
<html lang="en">
<head>
<meta charset="utf-8">
<title>Sweet Chord Voicing – Thumbnail Concepts</title>
<link rel="stylesheet" href="https://fonts.googleapis.com/css2?family=Josefin+Sans:wght@700&family=Arimo:wght@400&display=swap">
<style>
  :root {
    --teal: #2fb3a0;
    --teal-light: #57c8b7;
    --teal-dark: #1f8a7a;
    --ink: #221a1e;
    --red: #e2222a;
    --white: #ffffff;
    --paper: #ffffff;
    --skin: #e7bfa6;
    --shirt: #cdeee8;
  }
  html, body {
    margin: 0;
    padding: 0;
    width: 1200px;
    height: 2663px;
    overflow: hidden;
    background: var(--paper);
  }
  .sheet { display: block; width: 1200px; height: 2663px; }
  .variant-label {
    font-family: "Arimo", Arial, sans-serif;
    font-size: 24px;
    fill: #000;
  }
  .title {
    font-family: "Josefin Sans", "Montserrat", sans-serif;
    font-weight: 700;
    fill: var(--white);
    stroke: var(--red);
    stroke-width: 3px;
    paint-order: stroke;
    stroke-linejoin: round;
    filter: url(#red-glow);
  }
  .fill-teal { fill: var(--teal); }
  .fill-teal-light { fill: var(--teal-light); }
  .fill-teal-dark { fill: var(--teal-dark); }
  .fill-ink { fill: var(--ink); }
  .fill-red { fill: var(--red); }
  .frame-red { fill: none; stroke: var(--red); stroke-width: 5; }
  .arrow { fill: var(--white); stroke: var(--red); stroke-width: 2.5; stroke-linejoin: round; }
  .photo { fill: url(#photo-tones); }
</style>
</head>
<body>
<svg class="sheet" viewBox="0 0 680 1509" xmlns="http://www.w3.org/2000/svg">
  <defs>
    <filter id="red-glow" x="-20%" y="-20%" width="140%" height="140%">
      <feDropShadow dx="0" dy="0" stdDeviation="2" flood-color="#e2222a"/>
    </filter>
    <filter id="drop" x="-10%" y="-10%" width="130%" height="130%">
      <feDropShadow dx="3" dy="4" stdDeviation="3" flood-color="#000" flood-opacity="0.45"/>
    </filter>
    <linearGradient id="photo-tones" x1="0" y1="0" x2="0.6" y2="1">
      <stop offset="0" stop-color="#e7bfa6"/>
      <stop offset="0.45" stop-color="#d9e9e3"/>
      <stop offset="0.8" stop-color="#c7ebe4"/>
      <stop offset="1" stop-color="#2b2a2e"/>
    </linearGradient>
    <pattern id="stripes" width="16" height="16" patternUnits="userSpaceOnUse" patternTransform="rotate(20)">
      <rect width="16" height="16" fill="#2fb3a0"/>
      <rect width="6" height="16" fill="#1f8a7a"/>
    </pattern>
    <pattern id="stripes-wide" width="40" height="40" patternUnits="userSpaceOnUse" patternTransform="rotate(35)">
      <rect width="40" height="40" fill="#2fb3a0"/>
      <rect width="14" height="40" fill="#6ccfc0"/>
    </pattern>
  </defs>

  <!-- Concept A -->
  <g class="concept concept-a">
    <text class="variant-label" x="84" y="70">a</text>
    <polygon class="fill-red" points="88,76 585,76 598,360 110,360"/>
    <polygon class="fill-teal" points="96,82 578,82 590,352 116,352"/>
    <polygon class="fill-teal-light" points="96,82 160,82 110,200" opacity="0.5"/>
    <polygon class="fill-ink" points="348,86 576,86 588,348 300,348"/>
    <rect class="photo" x="150" y="90" width="280" height="258" rx="30" role="img" aria-label="Photo of the pianist seated at a keyboard, seen from above"/>
    <g transform="translate(470 215) rotate(-58)">
      <text class="title" text-anchor="middle" y="-38" font-size="40">SWEET</text>
      <text class="title" text-anchor="middle" y="6" font-size="40">CHORD</text>
      <text class="title" text-anchor="middle" y="50" font-size="40">VOICING</text>
    </g>
    <path class="arrow" transform="translate(545 305) rotate(-45)" d="M-22,-6 L4,-6 L4,-16 L24,0 L4,16 L4,6 L-22,6 Z"/>
  </g>

  <!-- Concept B -->
  <g class="concept concept-b">
    <text class="variant-label" x="84" y="414">b</text>
    <rect x="88" y="422" width="350" height="283" fill="url(#stripes)"/>
    <polygon class="fill-teal" points="250,422 598,422 598,470 300,470"/>
    <polygon class="fill-ink" points="440,422 598,422 598,705 305,705"/>
    <rect class="frame-red" x="90" y="464" width="340" height="239"/>
    <rect class="photo" x="140" y="445" width="275" height="260" rx="30" role="img" aria-label="Photo of the pianist seated at a keyboard, seen from above"/>
    <path class="arrow" d="M302,488 L340,488 L340,474 L374,505 L340,536 L340,522 L302,522 Z"/>
    <path class="fill-ink" d="M112,652 L126,664 L112,676 L118,664 Z"/>
    <g transform="translate(482 556) rotate(-56)">
      <text class="title" text-anchor="middle" y="-40" font-size="42">SWEET</text>
      <text class="title" text-anchor="middle" y="6" font-size="42">CHORD</text>
      <text class="title" text-anchor="middle" y="52" font-size="42">VOICING</text>
    </g>
  </g>

  <!-- Concept C -->
  <g class="concept concept-c">
    <text class="variant-label" x="88" y="774">c</text>
    <rect class="fill-teal" x="90" y="782" width="430" height="278"/>
    <polygon points="440,782 510,800 520,900 430,880" fill="url(#stripes)"/>
    <polygon class="fill-red" points="430,990 525,1000 520,1060 415,1060"/>
    <rect class="photo" x="110" y="790" width="330" height="270" rx="30" role="img" aria-label="Photo of the pianist seated at a keyboard, seen from above"/>
    <g filter="url(#drop)">
      <polygon class="fill-teal" points="290,826 565,826 600,1006 336,1006"/>
      <polygon class="fill-ink" points="298,834 556,834 588,998 342,998"/>
    </g>
    <text class="title" x="438" y="876" text-anchor="middle" font-size="48">SWEET</text>
    <text class="title" x="426" y="927" text-anchor="middle" font-size="48">CHORD</text>
    <text class="title" x="412" y="978" text-anchor="middle" font-size="48">VOICING</text>
  </g>

  <!-- Concept D -->
  <g class="concept concept-d">
    <text class="variant-label" x="84" y="1130">d</text>
    <polygon class="fill-teal-dark" points="90,1135 478,1135 555,1420 168,1420"/>
    <polygon points="128,1135 440,1135 505,1380 200,1380" fill="url(#stripes-wide)"/>
    <rect class="photo" x="168" y="1150" width="262" height="270" rx="30" role="img" aria-label="Photo of the pianist seated at a keyboard, seen from above"/>
    <g filter="url(#drop)">
      <polygon class="fill-red" points="345,1145 598,1145 598,1338 370,1338 320,1220"/>
      <polygon class="fill-ink" points="356,1152 598,1152 598,1330 376,1330 330,1222"/>
    </g>
    <path class="arrow" d="M284,1176 L314,1176 L314,1162 L342,1188 L314,1214 L314,1200 L284,1200 Z"/>
    <text class="title" x="576" y="1212" text-anchor="end" font-size="48">SWEET</text>
    <text class="title" x="576" y="1263" text-anchor="end" font-size="48">CHORD</text>
    <text class="title" x="576" y="1314" text-anchor="end" font-size="48">VOICING</text>
  </g>
</svg>
</body>
</html>
```